RUXO9 biz card & Stationery

UXO9 is a personalized shopping experience brought to you, that lets you find and discover fashion goods through a collection of boutiques curated by taste-makers - celebrities, stylists, designers, and fashion bloggers. Boutiques uses visual technology to help fashionistas discover and shop their look and creates the opportunity for designers to showcase their collections and latest inspirations online.

RUXO9 is built on technology developed by our team of fashion experts who work with engineers to “teach” our computer systems to understand various patterns, pairings, and genre definitions. When signed into your account, RUXO9 learns about your style and preferences and in turn, provides you better results and recommendations over time. Ultimately, RUXO9 will provide shoppers with a much richer and interactive shopping experience and help drive traffic to retailers' websites.

We need a definitely cool business card. The card must be black! And must use our official logo which can be download from RUXO9.com

The address for Letter head and evenlop, please use 4821 Larkmoor Avenue, Sutie 520 Los Angeles CA90012, email will be anyone@RUXO9.com, website is www.RUXO9.com

thanks

We received some of the design, thanks. But most of the design are not what we want. We need a very clean version with black ground, you may also use some dark gray to add the element. please take a look at http://bleckvorn.no/work/#tarvik__olmstrup/, we do like this kind of design very much. hope it help.

```html
<!DOCTYPE html>
<html lang="en">
<head>
<meta charset="utf-8">
<title>RUXO9 Stationery — Letterhead &amp; Envelope</title>
<link rel="stylesheet" href="https://fonts.googleapis.com/css2?family=Tenor+Sans&display=swap">
<style>
  :root {
    --ink: #000000;
    --paper: #ffffff;
    --reverse: #ffffff;
    --line: #1a1a1a;
  }
  * { margin: 0; padding: 0; box-sizing: border-box; }
  html, body { width: 1200px; height: 900px; overflow: hidden; background: var(--paper); }
  .canvas {
    position: relative; width: 1200px; height: 900px; background: var(--paper);
    font-family: "Tenor Sans", sans-serif; font-weight: 400;
  }

  /* Letterhead */
  .letterhead {
    position: absolute; left: 536px; top: 26px; width: 658px; height: 848px;
    background: var(--paper); border: 1.5px solid var(--line);
  }
  .letterhead__band {
    position: absolute; right: 0; top: 0; width: 185px; height: 100%;
    background: var(--ink); color: var(--reverse); padding: 14px 0 0 13px;
  }
  .letterhead .brand-name { font-size: 34px; line-height: 1; }
  .letterhead .contact { font-size: 8px; line-height: 1.45; margin-top: 12px; }

  /* Envelope */
  .envelope { position: absolute; left: 56px; top: 188px; width: 808px; height: 506px; }
  .envelope__flap { position: absolute; left: 0; top: 0; width: 808px; height: 108px; }
  .envelope__body {
    position: absolute; left: 0; top: 106px; width: 808px; height: 400px;
    background: var(--paper); border: 1.5px solid var(--line);
  }
  .envelope__band {
    position: absolute; left: 0; bottom: 0; width: 100%; height: 88px;
    background: var(--ink); color: var(--reverse);
    display: flex; justify-content: space-between; align-items: flex-end;
    padding: 0 14px 16px 13px;
  }
  .envelope .contact { font-size: 8px; line-height: 1.45; }
  .envelope .contact__web { display: block; text-align: right; }
  .envelope .brand-name { font-size: 46px; line-height: 1; }
</style>
</head>
<body>
<main class="canvas">
  <section class="letterhead" aria-label="Letterhead">
    <div class="letterhead__band">
      <div class="brand-name">RUXO9</div>
      <p class="contact">4821 Larkmoor Avenue,<br>Sutie 520 Los Angeles CA90012<br>www.RUXO9.com</p>
    </div>
  </section>

  <section class="envelope" aria-label="Envelope">
    <svg class="envelope__flap" viewBox="0 0 808 108" aria-hidden="true">
      <path d="M0.75 107 L46 14 Q52 1 66 1 L742 1 Q756 1 762 14 L807.25 107 Z"
            fill="#ffffff" stroke="#1a1a1a" stroke-width="1.5"/>
    </svg>
    <div class="envelope__body">
      <div class="envelope__band">
        <p class="contact">4821 Larkmoor Avenue,<br>Sutie 520 Los Angeles CA90012<span class="contact__web">www.RUXO9.com</span></p>
        <div class="brand-name">RUXO9</div>
      </div>
    </div>
  </section>
</main>
</body>
</html>
```